carpet cleaning flyer/leaflet modern/upmarket twist

We are Velvet Nest, We do carpet & upholstery cleaning for the domestic market, if you are able to incorporate images like the ones I have provided that would be awesome, please feel free to find similar! mine are only examples. id like a front cover photo with the company name running through it, and the back to be half picture and then the detailing of what we do which is in the document I've uploaded
Target Market(s)
Domestic house hold
Industry/Entity Type
Cleaning Service
Colors
eea4c8
e667a6
c3c3c3
cbcbcb
aaaaaa
f59296
Requirements
Must have
- It must be 2 sided also have A modern but upmarket feel, a luxury. a front picture with name on it, back page with picture and writing from the word document.
Nice to have
- a input from yourselves, your twist on it

```html
<!DOCTYPE html>
<html lang="en">
<head>
<meta charset="utf-8">
<title>Velvet Nest – Carpet &amp; Upholstery Cleaning Flyer</title>
<link rel="stylesheet" href="https://fonts.googleapis.com/css2?family=Jost:wght@400;500;700&family=Didact+Gothic&display=swap">
<style>
  :root {
    --pink: #e667a6;
    --pink-soft: #eea4c8;
    --carpet-dark: #aaaaaa;
    --carpet-mid: #b4b4b4;
    --carpet-light: #cbcbcb;
    --band: rgba(235, 235, 235, 0.55);
    --ink: #333333;
    --ink-deep: #1e1e1e;
    --page: #ffffff;
  }
  * { margin: 0; padding: 0; box-sizing: border-box; }
  html, body {
    width: 840px;
    height: 1200px;
    overflow: hidden;
    background: var(--page);
  }
  .canvas {
    position: relative;
    width: 840px;
    height: 1200px;
  }
  .card {
    position: absolute;
    left: 25px;
    width: 790px;
    overflow: hidden;
    box-shadow: 0 2px 6px rgba(0, 0, 0, 0.35);
  }
  .card--front { top: 25px; height: 558px; }
  .card--back  { top: 608px; height: 564px; }

  .carpet-photo {
    position: absolute;
    inset: 0;
    background:
      radial-gradient(ellipse at 15% 30%, #bdbdbd 0%, transparent 60%),
      linear-gradient(160deg, var(--carpet-mid) 0%, var(--carpet-dark) 100%);
  }
  .cleaned-band {
    position: absolute;
    background: var(--band);
  }
  .card--front .cleaned-band { left: 190px; right: 0; top: 70px; height: 342px; }
  .card--back .cleaned-band  { left: 0; right: 0; top: 70px; height: 345px; }

  .nozzle-area {
    position: absolute;
    left: 10px; top: 70px;
    width: 185px; height: 345px;
    background: linear-gradient(90deg, #3a3a3a 0%, #555555 60%, #444444 100%);
    border-radius: 10px;
    opacity: 0.85;
  }

  .brand-title {
    position: absolute;
    left: 232px;
    top: 128px;
    font-family: "Jost", sans-serif;
    font-weight: 700;
    font-size: 96px;
    line-height: 84px;
    color: var(--pink);
    letter-spacing: 1px;
    text-transform: uppercase;
  }
  .brand-tagline {
    position: absolute;
    left: 233px;
    top: 318px;
    font-family: "Jost", sans-serif;
    font-weight: 500;
    font-size: 36px;
    color: var(--ink);
    letter-spacing: 0.5px;
  }

  .step-numbers {
    position: absolute;
    left: 0; right: 0;
    top: 140px;
    display: flex;
    justify-content: space-around;
    padding: 0 40px;
    font-family: "Jost", sans-serif;
    font-weight: 700;
    font-size: 230px;
    line-height: 1;
    color: var(--pink-soft);
    opacity: 0.45;
  }
  .values {
    position: absolute;
    left: 10px; right: 10px;
    top: 112px;
    display: flex;
    justify-content: space-between;
  }
  .value {
    width: 255px;
    text-align: center;
  }
  .value__title {
    font-family: "Jost", sans-serif;
    font-weight: 700;
    font-size: 27px;
    color: var(--pink);
    letter-spacing: 0.5px;
    margin-bottom: 6px;
  }
  .value__text {
    font-family: "Didact Gothic", sans-serif;
    font-size: 15.5px;
    line-height: 16px;
    color: var(--ink-deep);
  }
  .back-brand {
    position: absolute;
    left: 0; right: 0;
    top: 352px;
    text-align: center;
    font-family: "Jost", sans-serif;
    font-weight: 700;
    font-size: 50px;
    color: var(--pink);
    letter-spacing: 1.5px;
    text-transform: uppercase;
  }
  .contact {
    position: absolute;
    left: 0; right: 0;
    top: 420px;
    text-align: center;
    font-family: "Didact Gothic", sans-serif;
    font-size: 20px;
    line-height: 23px;
    color: var(--ink-deep);
  }
</style>
</head>
<body>
<main class="canvas">

  <section class="card card--front">
    <div class="carpet-photo" role="img" aria-label="Photo of grey carpet with a freshly vacuumed stripe"></div>
    <div class="cleaned-band"></div>
    <div class="nozzle-area" role="img" aria-label="Photo of a vacuum cleaner head resting on the carpet"></div>
    <h1 class="brand-title">Velvet<br>Nest</h1>
    <p class="brand-tagline">Carpet &amp; Upholster Cleaning</p>
  </section>

  <section class="card card--back">
    <div class="carpet-photo" role="img" aria-label="Photo of grey carpet with a freshly vacuumed stripe"></div>
    <div class="cleaned-band"></div>
    <div class="step-numbers" aria-hidden="true"><span>1</span><span>2</span><span>3</span></div>

    <div class="values">
      <article class="value">
        <h2 class="value__title">RELIABLE</h2>
        <p class="value__text">We are fully insured to work in your home, we guarantee all our work so if any issues do arise we will do our up most to put it back right for you.</p>
      </article>
      <article class="value">
        <h2 class="value__title">PROFESSIONAL</h2>
        <p class="value__text">We use the latest hot water extraction cleaning technology to give us the ability to get into the ground down dirt deep down inside the Fibres.</p>
      </article>
      <article class="value">
        <h2 class="value__title">TRUSTWORTHY</h2>
        <p class="value__text">We pride ourselves on providing outstanding services to our customers. From a single carpet or rug,to a whole house clean, we provide a reliable and friendly service. Call us to discuss your needs.</p>
      </article>
    </div>

    <p class="back-brand">Velvet Nest</p>
    <address class="contact" style="font-style: normal;">
      Tel. 01632 960 418<br>
      anna.reed@velvetnest.co.uk
    </address>
  </section>

</main>
</body>
</html>
```